Home Remodeling company needs a business card design

we need a business card design for home remodeling company in hamilton county, indiana USA. we offers a wide range of construction services including whole house renovations, Design and Build Basements and Kitchen and Bathroom Remodeling . we would like to see designs for both site of business card that use the same color of the company logo and also including all information below :
1- Samir Daoudi CEO / General Contractor
2- all company contacts Telephone numbers ( 1-888-TOVAL-42 ) ( 317-555-0192) email address ( info@tovalhome.example) website ( www.tovalhome.example ) and social media logos (Facebook- twitter- google plus )
3- company logo
4- licensed . insured . bonded

```html
<!DOCTYPE html>
<html lang="en">
<head>
<meta charset="utf-8">
<title>Toval Home Remodeling — Business Card</title>
<link rel="stylesheet" href="https://fonts.googleapis.com/css2?family=Cabin:wght@400;600&display=swap">
<style>
  :root {
    --backdrop: #9c9d9d;
    --charcoal: #333436;
    --paper: #e4e5e9;
    --brand-red: #a8292f;
    --ink-light: #eceded;
    --icon-light: #cfd0d2;
    --ink-dark: #3a3b3e;
  }
  * { margin: 0; padding: 0; box-sizing: border-box; }
  html, body {
    width: 1105px; height: 1200px; overflow: hidden;
    background: var(--backdrop);
    font-family: "Cabin", "Gill Sans", sans-serif;
  }
  .card {
    position: absolute; left: 112px;
    width: 880px; height: 503px;
    overflow: hidden;
  }
  .card--front { top: 62px; background: var(--paper); }
  .card--back { top: 635px; background: var(--brand-red); }

  /* Front */
  .identity-panel {
    position: absolute; left: 0; top: 0;
    width: 427px; height: 100%;
    background: var(--charcoal);
  }
  .name-tab {
    position: absolute; left: 380px; top: 96px;
    width: 48px; height: 44px;
  }
  .holder {
    position: absolute; right: 513px; top: 88px;
    text-align: right; color: var(--ink-light);
  }
  .holder__name { font-size: 31px; font-weight: 600; letter-spacing: 0.3px; line-height: 1.2; }
  .holder__title { font-size: 24px; font-weight: 400; line-height: 1.3; }

  .contacts {
    position: absolute; right: 516px; top: 280px;
    list-style: none; color: var(--ink-light);
    font-size: 23px; line-height: 33px;
  }
  .contacts li { display: flex; justify-content: flex-end; align-items: center; }
  .contacts__text { text-align: right; }
  .contacts svg { width: 22px; height: 22px; margin-left: 20px; flex: none; }
  .contacts .icon-stroke { stroke: var(--icon-light); fill: none; stroke-width: 1.8; }
  .contacts .icon-fill { fill: var(--icon-light); }

  .wordmark {
    position: absolute; left: 480px; top: 226px;
    display: flex; align-items: center;
  }
  .wordmark__mark { width: 10px; height: 54px; background: var(--brand-red); margin-right: 12px; }
  .wordmark__name {
    font-size: 40px; font-weight: 600; letter-spacing: 2px;
    color: var(--ink-dark); text-transform: uppercase;
  }

  /* Back */
  .emblem-block {
    position: absolute; left: 359px; top: 145px;
    width: 154px; height: 156px;
    background: var(--paper);
  }
  .credentials {
    position: absolute; left: 0; right: 0; top: 375px;
    text-align: center; color: var(--ink-light);
    font-size: 26px; letter-spacing: 0.5px;
  }
  .social-row {
    position: absolute; left: 315px; top: 423px;
    width: 250px; height: 34px;
  }
</style>
</head>
<body>
  <section class="card card--front" aria-label="Card front">
    <div class="identity-panel"></div>
    <svg class="name-tab" viewBox="0 0 48 44" aria-hidden="true">
      <polygon points="0,22 20,0 48,0 48,44 20,44" fill="var(--paper)"/>
      <rect x="22" y="17" width="11" height="11" fill="var(--brand-red)"/>
    </svg>

    <div class="holder">
      <p class="holder__name">Samir Daoudi</p>
      <p class="holder__title">CEO / General Contractor</p>
    </div>

    <ul class="contacts">
      <li><span class="contacts__text">1-888-TOVAL-42</span>
        <svg viewBox="0 0 24 24" aria-hidden="true"><path class="icon-fill" d="M6.6 2.5l3 3.2-1.9 2.4c1.3 2.8 3.4 4.9 6.2 6.2l2.4-1.9 3.2 3-2 3.6C10.4 18.6 5.4 13.6 3 6.5z"/></svg></li>
      <li><span class="contacts__text">317-555-0192</span>
        <svg viewBox="0 0 24 24" aria-hidden="true"><rect class="icon-stroke" x="6.5" y="2" width="11" height="20" rx="1.5"/><line class="icon-stroke" x1="10" y1="18.5" x2="14" y2="18.5"/></svg></li>
      <li><span class="contacts__text">info@tovalhome.example</span>
        <svg viewBox="0 0 24 24" aria-hidden="true"><rect class="icon-stroke" x="2.5" y="5.5" width="19" height="13"/><polyline class="icon-stroke" points="2.5,5.5 12,13 21.5,5.5"/></svg></li>
      <li><span class="contacts__text">www.tovalhome.example</span>
        <svg viewBox="0 0 24 24" aria-hidden="true"><circle class="icon-stroke" cx="12" cy="12" r="9.5"/><ellipse class="icon-stroke" cx="12" cy="12" rx="4" ry="9.5"/><line class="icon-stroke" x1="2.5" y1="12" x2="21.5" y2="12"/></svg></li>
    </ul>

    <div class="wordmark">
      <span class="wordmark__mark"></span>
      <span class="wordmark__name">Toval Home Remodeling</span>
    </div>
  </section>

  <section class="card card--back" aria-label="Card back">
    <div class="emblem-block"></div>
    <p class="credentials">LICENSED | INSURED | BONDED</p>
    <svg class="social-row" viewBox="0 0 250 34" aria-label="Social media links">
      <line x1="10" y1="17" x2="70" y2="17" stroke="var(--icon-light)" stroke-width="1.5"/>
      <line x1="180" y1="17" x2="240" y2="17" stroke="var(--icon-light)" stroke-width="1.5"/>
      <circle cx="86" cy="17" r="15" fill="var(--paper)"/>
      <circle cx="122" cy="17" r="15" fill="var(--paper)"/>
      <circle cx="159" cy="17" r="15" fill="var(--paper)"/>
    </svg>
  </section>
</body>
</html>
```